New UI for electricity data tool

We are looking for a new UI for the website http://voltmeadow.net. Reassessing the structure of the website is as important as specific design choices. We have created a uniquely comprehensive set of global electricity generation data and now we are looking for creative solutions for how to make this data accessible. Researching and referencing other similar projects may be a good idea.

Goals:
• The website should clearly communicate the most important general conclusions that can be drawn from the data, including:
◦ The world as a whole is not moving away from fossil fuels for electricity generation
◦ There are substantial differences between regions
▪ Some regions have basically solved the problem – they already generate almost all of their electricity from non-fossil sources
▪ Some regions have greatly improved in terms of decarbonizing their electricity generation.
▪ Some regions have greatly deteriorated, in other words they are using a much higher share of fossil fuels to generate their electricity.
◦ There are substantial differences between energy sources. Regions that have successfully decarbonized their electricity generation have usually done so using hydro and/or nuclear. Other low-carbon energy sources have grown quickly in relative terms in the last few years but are so far contributing little in absolute numbers.
• The website should serve as inspiration for energy policy debates. The goal is to study the impact of existing policies around the world. Energy policy here refers to particular combinations of energy sources – ie how much have the countries invested in each type of electricity generation. The tool should help answer questions such as:
◦ Which countries have done the most in terms of decarbonizing their electricity generation?
◦ Which types of energy polices have lead to the fastest decarbonization processes around the world?
◦ If country A changed its energy policy to be more like country B, what would the likely impact be?

Challenges:
• There is a lot of data – it can be overwhelming to the user. It’s crucial to make the site easy to navigate. The main page should highlight the most important data, and it should also be straightforward to find more detailed data.
• Data availability varies from region to region. The current interface addresses this with the default option “Exclude regions with limited data”. We expect a better approach to dealing with this issue. For some regions and years energy sources are grouped together as for example “other renewables” whereas in other cases more detailed data is available.
• Credibility is crucial. Our data is based on a combination of data from KQ and the Tessaro Fund. It must be very clear throughout the site where each data set comes from.

Details:
• The current chart color schemes is loosely based on the carbon emissions from each energy source. This should not necessarily be so. The goal is to on the one hand communicate clearly the amounts of fossil vs non-fossil energy that are generated by each region. At the same time we also want to make it easy to view specific energy sources.

Inspirational websites:
• https://www.trendlooper.org/
• https://pelmarstatix.org/

Let's simplify. The main metric to focus on is Fernhollow Watt and the extent to which the world and each country has achieved it (eg Iceland 100%, France 88% and so on). I'm considering changing the name of the site to FernhollowWatt.org. We can use maps, charts and perhaps other tools to communicate this main message. What's the best way of doing this?

```html
<!DOCTYPE html>
<html lang="en">
<head>
<meta charset="utf-8">
<title>VoltMeadow – Regions</title>
<link href="https://fonts.googleapis.com/css2?family=Lato:wght@400;700&display=swap" rel="stylesheet">
<style>
:root{
  --page:#ffffff;
  --card:#f5f5f5;
  --panel:#ffffff;
  --ink:#2b2b33;
  --muted:#6d6d78;
  --accent:#5a40d8;
  --line:#e2e2ea;
  --track:#d8d8e2;
  --nonfossil:#42d3a0;
  --hydro:#2bbcf5;
  --nuclear:#ff2a5f;
  --wind:#ff2ce0;
  --oil:#ff7a2a;
  --solar:#f5e200;
  --fossil:#333338;
  --other:#777780;
}
*{box-sizing:border-box;margin:0;padding:0}
html,body{width:1200px;height:675px;overflow:hidden;background:var(--page);font-family:"Lato",sans-serif;color:var(--ink)}
.stage{position:relative;width:1200px;height:675px}
.app{position:absolute;left:150px;top:84px;width:900px;height:506px;background:var(--card);border-radius:24px;box-shadow:0 14px 40px rgba(40,40,70,.08)}
.abs{position:absolute}
.plot{position:absolute;left:0;top:0}
.plot text{font-family:"Lato",sans-serif}
.plot .axis{font-size:6px;fill:var(--muted)}
.plot .year{font-size:7px;fill:var(--accent)}
.brand{left:38px;top:24px;font-size:11px;color:var(--accent);letter-spacing:.2px}
.menu{left:854px;top:27px}
.section-title{left:49px;top:67px;font-size:11.5px;font-weight:700;letter-spacing:.3px}
.section-title span{color:var(--accent)}
.more{left:216px;top:66px;color:var(--accent);font-size:11px;letter-spacing:1px;font-weight:700}
.pill{position:absolute;border:1px solid var(--accent);border-radius:20px;display:flex;align-items:center;font-size:8px;color:var(--muted)}
.country{left:49px;top:97px;width:177px;height:24px;padding-left:11px;color:var(--ink);font-weight:700;font-size:8.5px}
.flag{display:flex;width:20px;height:12px;margin-right:6px}
.flag i{flex:1}
.chev{position:absolute;right:11px;top:8px}
.search{left:246px;top:62px;width:200px;height:24px;padding-left:22px}
.search svg{position:absolute;left:8px;top:6px}
.sort{left:713px;top:62px;width:80px;height:24px;padding-left:7px;color:var(--accent)}
.show{left:801px;top:62px;width:62px;height:24px;padding-left:7px;color:var(--accent)}
.share{left:384px;top:121px;display:flex;align-items:center;gap:8px;font-size:7.5px;font-weight:700;color:var(--accent);letter-spacing:.5px}
.legend{left:49px;top:166px;list-style:none}
.legend li{display:flex;align-items:center;height:25.8px;font-size:8px}
.legend i{width:7px;height:7px;border-radius:50%;margin-right:6px;margin-left:1px}
.panel{position:absolute;background:var(--panel);border-radius:6px}
.insight{left:662px;top:158px;width:201px;height:97px}
.insight p{position:absolute;left:7px;top:11px;width:188px;font-size:7.3px;line-height:13px;color:var(--muted);letter-spacing:.2px}
.insight p b{font-weight:400;color:var(--accent)}
.btn{position:absolute;display:flex;align-items:center;background:var(--accent);color:#fff;border-radius:14px;font-size:7.5px;font-weight:700;letter-spacing:.4px}
.btn .ico{width:18px;height:18px;border-radius:50%;background:#fff;margin:0 9px 0 3px;display:flex;align-items:center;justify-content:center}
.read{left:55px;top:62px;width:91px;height:24px}
.sources{left:662px;top:264px;width:201px;height:116px}
.sources h3{position:absolute;left:7px;top:7px;font-size:8.5px;font-weight:700;letter-spacing:.3px}
.sources .all{position:absolute;right:7px;top:8px;font-size:7px;color:var(--accent)}
.sources svg{position:absolute;left:0;top:0}
.sources svg text{font-family:"Lato",sans-serif;font-size:6.5px;fill:var(--ink)}
.sources svg .tick{font-size:6px;fill:var(--muted)}
.powered{left:49px;top:405px;font-size:7.5px;font-weight:700;letter-spacing:.6px}
.partners{left:49px;top:421px;display:flex;align-items:center;gap:14px;font-size:7.5px;font-weight:700;color:#1f3a60}
.partners span{display:flex;align-items:center;gap:4px}
.partners i{display:block;width:13px;height:13px;border-radius:50%;background:#1f3a60}
.note{left:49px;top:463px;font-size:6.5px;color:var(--muted)}
.note b{color:var(--accent);font-weight:400}
.download{left:705px;top:422px;width:115px;height:24px}
.caption{position:absolute;left:0;width:1200px;top:616px;text-align:center;font-size:11px;color:var(--accent);letter-spacing:.5px}
</style>
</head>
<body>
<div class="stage">
  <main class="app">
    <svg class="plot" width="900" height="506" viewBox="0 0 900 506" aria-label="Electricity share by source for France, with year timeline">
      <g class="axis" text-anchor="end">
        <text x="261" y="170">100%</text><text x="261" y="190">90%</text><text x="261" y="211">80%</text>
        <text x="261" y="231">70%</text><text x="261" y="251">60%</text><text x="261" y="271">50%</text>
        <text x="261" y="292">40%</text><text x="261" y="312">30%</text><text x="261" y="332">20%</text>
        <text x="261" y="352">10%</text><text x="261" y="373">0%</text>
      </g>
      <line x1="264.5" y1="164" x2="264.5" y2="375" stroke="var(--line)"/>
      <line x1="264" y1="374.5" x2="636" y2="374.5" stroke="var(--line)"/>
      <rect x="284" y="183.5" width="13" height="187" fill="var(--nonfossil)"/>
      <rect x="338" y="343" width="13" height="27.5" fill="var(--hydro)"/>
      <rect x="391" y="224" width="13" height="146.5" fill="var(--nuclear)"/>
      <rect x="445" y="366" width="13" height="4.5" fill="var(--solar)"/>
      <rect x="498" y="361" width="13" height="9.5" fill="var(--wind)"/>
      <rect x="551" y="363.5" width="13" height="7" fill="var(--other)"/>
      <rect x="605" y="355" width="13" height="15.5" fill="var(--fossil)"/>

      <circle cx="255" cy="434" r="10" fill="var(--accent)"/>
      <path d="M252.5 430.5v7l5.5-3.5z" fill="none" stroke="#fff" stroke-width="1"/>
      <g stroke="var(--track)" stroke-width="1.2">
        <line x1="270" y1="434" x2="305" y2="434"/><line x1="309" y1="434" x2="344" y2="434"/>
        <line x1="348" y1="434" x2="383" y2="434"/><line x1="387" y1="434" x2="422" y2="434"/>
        <line x1="426" y1="434" x2="461" y2="434"/><line x1="465" y1="434" x2="500" y2="434"/>
        <line x1="504" y1="434" x2="539" y2="434"/>
        <line x1="581" y1="434" x2="616" y2="434"/><line x1="620" y1="434" x2="655" y2="434"/>
      </g>
      <line x1="542" y1="434" x2="577" y2="434" stroke="var(--accent)" stroke-width="1.4"/>
      <text class="year" x="559.5" y="447" text-anchor="middle">2018</text>
    </svg>

    <div class="abs brand"><b>VoltMeadow</b>.net</div>
    <svg class="abs menu" width="11" height="9" viewBox="0 0 11 9" aria-label="Menu"><g stroke="#5a40d8" stroke-width="1.3" stroke-linecap="round"><line x1="1" y1="1" x2="10" y2="1"/><line x1="3" y1="4.5" x2="10" y2="4.5"/><line x1="1" y1="8" x2="10" y2="8"/></g></svg>

    <div class="abs section-title">Top Regions <span>*</span></div>
    <div class="abs more">···</div>
    <div class="pill country"><span class="flag"><i style="background:#3d3fa0"></i><i style="background:#f5f5f5"></i><i style="background:#ff3b4e"></i></span>France
      <svg class="chev" width="6" height="6" viewBox="0 0 6 6"><path d="M1 2l2 2 2-2" fill="none" stroke="#5a40d8" stroke-width="1"/></svg></div>

    <div class="pill search"><svg width="10" height="10" viewBox="0 0 10 10"><circle cx="4.3" cy="4.3" r="3.4" fill="none" stroke="#5a40d8" stroke-width="1.1"/><line x1="6.8" y1="6.8" x2="9.2" y2="9.2" stroke="#5a40d8" stroke-width="1.1"/></svg>Search countries</div>
    <div class="pill sort">Sort by<svg class="chev" width="6" height="6" viewBox="0 0 6 6"><path d="M1 2l2 2 2-2" fill="none" stroke="#5a40d8" stroke-width="1"/></svg></div>
    <div class="pill show">Show '%'<svg class="chev" width="6" height="6" viewBox="0 0 6 6"><path d="M1 2l2 2 2-2" fill="none" stroke="#5a40d8" stroke-width="1"/></svg></div>

    <div class="abs share"><svg width="14" height="13" viewBox="0 0 14 13"><path d="M1 6v6h12V9" fill="none" stroke="#5a40d8" stroke-width="1.2"/><path d="M4 8c1-3 4-4 7-4M9 1.5l2.5 2.5L9 6.5" fill="none" stroke="#5a40d8" stroke-width="1.2"/></svg>SHARE OR EMBED THIS VIEW</div>

    <ul class="abs legend">
      <li><i style="background:var(--nonfossil)"></i>Non-fossil</li>
      <li><i style="background:var(--hydro)"></i>Hydro</li>
      <li><i style="background:var(--nuclear)"></i>Nuclear</li>
      <li><i style="background:var(--wind)"></i>Wind</li>
      <li><i style="background:var(--oil)"></i>Oil</li>
      <li><i style="background:var(--solar)"></i>Solar</li>
      <li><i style="background:var(--fossil)"></i>Unspecified fossil fuels</li>
      <li><i style="background:var(--other)"></i>Other renewables</li>
    </ul>

    <section class="panel insight">
      <p><b>88%</b> of the electricity in France is generated from <b>Fernhollow Watt</b>. The primary low-carbon power source is nuclear.</p>
      <div class="btn read"><span class="ico"><svg width="9" height="9" viewBox="0 0 9 9"><path d="M4 1.5H1.5v6h6V5M5.5 1h2.5v2.5M8 1L4.5 4.5" fill="none" stroke="#5a40d8" stroke-width="1"/></svg></span>READ MORE</div>
    </section>

    <section class="panel sources">
      <h3>Energy Sources</h3>
      <span class="all">View All Regions</span>
      <svg width="201" height="116" viewBox="0 0 201 116">
        <line x1="7" y1="24" x2="7" y2="99" stroke="#e2e2ea"/>
        <line x1="7" y1="99" x2="195" y2="99" stroke="#e2e2ea"/>
        <text x="12" y="33">Nuclear</text>
        <rect x="7" y="38.5" width="140" height="7" fill="var(--nuclear)"/>
        <text x="12" y="70">Fernhollow Watt</text>
        <rect x="7" y="75.5" width="154" height="7" fill="var(--nonfossil)"/>
        <text class="tick" x="7" y="110">0%</text>
        <text class="tick" x="100" y="110" text-anchor="middle">50%</text>
        <text class="tick" x="194" y="110" text-anchor="end">100%</text>
      </svg>
    </section>

    <div class="abs powered">POWERED BY</div>
    <div class="abs partners"><span><i style="background:#6ab82a"></i>KQ</span><span><i></i>TESSARO FUND</span></div>
    <div class="abs note"><b>*</b> Excluding regions with limited data.</div>

    <div class="btn download"><span class="ico"><svg width="10" height="9" viewBox="0 0 10 9"><path d="M2.8 6.5H2a1.8 1.8 0 0 1 0-3.6 2.8 2.8 0 0 1 5.4-.6A1.9 1.9 0 0 1 8 6.5h-.8M5 4v4.5M3.6 7.2 5 8.5l1.4-1.3" fill="none" stroke="#5a40d8" stroke-width=".9"/></svg></span>DOWNLOAD DATA</div>
  </main>
  <div class="caption">Regions</div>
</div>
</body>
</html>
```